MOVIE POSTER - PSYCHOLOGICAL THRILLER

I'm looking for an epic, original movie poster design for our independent feature film THE LOOM.

The Film is a psychological thriller dealing with sex trafficking.

The story is about two rival prostitutes joining forces to help their fellow 9 year-old captor escape from THE LOOM. They are held by THE GUARD, who's face we never real see completely.

The lead character is the woman in the yellow dress.
Supporting character has the black top
The little girl is in the blue shirt
The guard is the old guy with the tattoos.

You don't need all the characters.
Or even the main characters.
I just want a great design.

Images are attached but there are a BUNCH MORE on the link below.
The images are held on my nimbus locker here:
https://locker.nimbusvault.example/open?id=7Qr2_TpzWmN84XkaVd3C6YhuEf1J

The film was shot in 4K, so I can pull film grabs if need be.

The color scheme right now favors move warm colors. But we're open to other ideas.
Really would like to see a bold concept that will show up well as a thumbnail image on places like shopvale and reelbox.

The dimension need to be 27x40" in CMYK format.
I'll be requiring both a high resolution jpeg and the working adobe files with the working layers intact.

Thank you in advance.

Target Market(s)

Psychological Thriller Movie Fans

Industry/Entity Type

Movie Production

Requirements
Must have
• Title, log line and credit block
Nice to have
• All the characters but not required.
• I care more about an effective design
Should not have
• none

```html
<!DOCTYPE html>
<html lang="en">
<head>
<meta charset="utf-8">
<title>THE LOOM — Poster</title>
<link href="https://fonts.googleapis.com/css2?family=Anton&family=Oswald:wght@400;500&display=swap" rel="stylesheet">
<style>
  :root {
    --paper: #e9ddb8;
    --ink: #111010;
    --rust: #7b3e22;
    --credit: #6d6a63;
    --photo-light: #d9a777;
    --photo-mid: #a8623a;
    --photo-dark: #5a3420;
    --dress: #e3c42a;
  }
  html, body { margin: 0; padding: 0; overflow: hidden; background: var(--paper); }
  .poster {
    position: relative;
    width: 840px;
    height: 1200px;
    overflow: hidden;
    background: var(--paper);
  }
  .portrait {
    position: absolute;
    left: 0;
    top: 200px;
    width: 450px;
    height: 1000px;
  }
  .type-layer {
    position: absolute;
    left: 0;
    top: 0;
    width: 840px;
    height: 1200px;
  }
  .title {
    font-family: "Anton", "Impact", sans-serif;
    font-size: 190px;
    fill: var(--ink);
  }
  .tagline {
    font-family: "Oswald", "Arial Narrow", sans-serif;
    font-weight: 500;
    font-size: 44px;
    fill: var(--rust);
  }
  .status {
    font-family: "Oswald", "Arial Narrow", sans-serif;
    font-weight: 500;
    font-size: 24px;
    fill: var(--credit);
  }
  .date {
    font-family: "Oswald", "Arial Narrow", sans-serif;
    font-weight: 400;
    font-size: 54px;
    fill: var(--rust);
  }
  .credit {
    font-family: "Oswald", "Arial Narrow", sans-serif;
    font-weight: 500;
    font-size: 19px;
    fill: var(--credit);
  }
  .credit .role {
    font-size: 7px;
    font-weight: 400;
  }
</style>
</head>
<body>
<main class="poster">
  <svg class="portrait" viewBox="0 0 450 1000" role="img" aria-label="Portrait photograph of the lead woman with auburn hair in a yellow dress, looking sideways">
    <defs>
      <linearGradient id="hair-tone" x1="0" y1="0" x2="1" y2="1">
        <stop offset="0" stop-color="var(--photo-dark)"/>
        <stop offset="0.45" stop-color="var(--photo-mid)"/>
        <stop offset="1" stop-color="var(--photo-light)"/>
      </linearGradient>
    </defs>
    <path d="M0 40 Q180 -20 330 90 Q440 220 420 520 Q400 600 330 640 L380 790 L420 1000 L0 1000 Z" fill="url(#hair-tone)"/>
    <path d="M0 830 Q200 800 360 830 L420 1000 L0 1000 Z" fill="var(--dress)"/>
  </svg>

  <svg class="type-layer" viewBox="0 0 840 1200">
    <text class="title" x="116" y="260" textLength="676" lengthAdjust="spacingAndGlyphs">THE LOOM</text>
    <text class="tagline" x="432" y="350" textLength="368" lengthAdjust="spacingAndGlyphs">“INSERRT YOUR TAGLINE HERE”</text>

    <text class="status" x="692" y="740" textLength="102" lengthAdjust="spacingAndGlyphs">COMING SOON</text>
    <text class="date" x="568" y="788" textLength="228" lengthAdjust="spacing">26.05.2017</text>

    <text class="credit" x="408" y="811" textLength="392" lengthAdjust="spacingAndGlyphs">AMBERLINE MEDIA &amp; ENTERTAINMENT <tspan class="role">presents a film by</tspan> CORIN VALE “RAFTERS OF ASH”</text>
    <text class="credit" x="450" y="839" textLength="350" lengthAdjust="spacingAndGlyphs">TAVIN HOLLIS <tspan class="role">music by</tspan> MARLO PENROSE DANE WHITLOW</text>
    <text class="credit" x="300" y="867" textLength="500" lengthAdjust="spacingAndGlyphs"><tspan class="role">costumes by</tspan> ILSE MARROW <tspan class="role">edited by</tspan> OTTO BRISK LENN DACOSTA RENO FAIRWEATHER</text>
    <text class="credit" x="300" y="893" textLength="500" lengthAdjust="spacingAndGlyphs"><tspan class="role">sound designed by</tspan> GASPARD LENOIR <tspan class="role">screenplay by</tspan> TAVIN HOLLIS</text>
    <text class="credit" x="540" y="923" textLength="260" lengthAdjust="spacingAndGlyphs"><tspan class="role">special thanks to</tspan> JORY TAMSIN BRAM SOLVIG KIA LUND</text>
    <text class="credit" x="442" y="951" textLength="358" lengthAdjust="spacingAndGlyphs">PELL SORENSEN NILS TREVANE LIO NYQUIST QUILL BARROW</text>
  </svg>
</main>
</body>
</html>
```